Sandwich Board and Poster design promoting a medical aesthetic clinic

I am looking for a clean, modern and relaxing design promoting a medical physician-led aesthetic clinic.
Services offered are neuromodulator treatment (Quelvo) and Dermal Fillers.
Logo must be included.
Use the tag line "Refresh your look, revive your spirit."
Address is 204-205 27361 92 Ave, Surrey, V7K 2M4
604-555-0148
email - info@lumawellpine.ca
www.lumawellpine.ca

```html
<!DOCTYPE html>
<html lang="en">
<head>
<meta charset="utf-8">
<title>Lumawell Poster</title>
<link href="https://fonts.googleapis.com/css2?family=Montserrat:wght@400;500;600;700;800&display=swap" rel="stylesheet">
<style>
  :root {
    --bg: #e9e7e3;
    --paper: #ffffff;
    --cream: #f8f4e8;
    --navy: #1f3a5c;
    --gold: #c9a227;
    --gold-light: #e2c45a;
    --ink: #1b1b1b;
    --white: #ffffff;
    --skin-light: #e7c3a8;
    --skin-mid: #c8977a;
    --skin-deep: #6b4633;
    --hair-dark: #3a2a22;
    --hair-blond: #d9c39a;
  }
  * { box-sizing: border-box; margin: 0; padding: 0; }
  html, body { width: 1200px; height: 1200px; overflow: hidden; }
  body {
    background: var(--bg);
    font-family: "Montserrat", sans-serif;
    position: relative;
  }
  .poster {
    position: absolute;
    left: 228px; top: 40px;
    width: 744px; height: 1120px;
    background: var(--paper);
    padding: 22px 24px;
    box-shadow: 0 4px 16px rgba(0,0,0,0.12);
  }
  .poster-body {
    width: 100%; height: 100%;
    display: flex; flex-direction: column;
    background: var(--cream);
  }
  .hero-photo {
    height: 382px;
    display: flex;
  }
  .hero-side { width: 36%; }
  .hero-side.left {
    background: linear-gradient(90deg, var(--hair-dark) 0%, var(--skin-light) 18%, #ecd2bd 45%, var(--skin-mid) 70%, #dcb49a 100%);
  }
  .hero-center {
    flex: 1;
    background: radial-gradient(ellipse at 50% 75%, #fdf9ee 0%, #f7efd9 60%, #f1e5c8 100%);
  }
  .hero-side.right {
    background: linear-gradient(90deg, #ecd3bf 0%, var(--hair-blond) 30%, #8a5a40 58%, var(--skin-deep) 80%, var(--hair-dark) 100%);
  }
  .brand {
    margin-top: 48px;
    display: flex;
    justify-content: center;
    align-items: center;
    gap: 20px;
  }
  .brand-mark {
    width: 16px; height: 16px;
    border-radius: 50%;
    background: var(--gold);
    flex: none;
  }
  .brand-name {
    font-size: 50px;
    font-weight: 500;
    letter-spacing: 16px;
    color: var(--navy);
    line-height: 1;
    margin-right: -16px;
  }
  .divider {
    height: 2px;
    margin: 42px auto 0;
    width: 560px;
    background: linear-gradient(90deg, rgba(0,0,0,0), rgba(0,0,0,0.12), rgba(0,0,0,0));
  }
  .tagline {
    margin-top: 18px;
    text-align: center;
    font-size: 38px;
    line-height: 1.25;
    font-weight: 800;
    color: var(--navy);
  }
  .divider.lower { margin-top: 16px; }
  .services {
    position: relative;
    margin: 30px auto 0;
    width: 496px;
    border: 1.5px solid var(--gold);
    border-radius: 10px;
    padding: 18px 20px 12px;
    text-align: center;
  }
  .services-title {
    position: absolute;
    top: -13px; left: 50%;
    transform: translateX(-50%);
    background: var(--cream);
    padding: 0 12px;
    white-space: nowrap;
    font-size: 20px;
    font-weight: 700;
    color: var(--gold);
  }
  .services-list {
    font-size: 22px;
    line-height: 1.4;
    font-weight: 500;
    color: var(--ink);
  }
  .treatment-strip {
    margin-top: auto;
    height: 160px;
    background: linear-gradient(90deg, var(--gold), var(--gold-light), var(--gold));
    padding: 10px 0;
    display: flex;
    gap: 10px;
  }
  .treatment-photo { flex: 1; }
  .treatment-photo.forehead { background: linear-gradient(90deg, #b58a70 0%, #c99a80 45%, #a9cde0 75%, #e9edf0 100%); }
  .treatment-photo.brow { background: linear-gradient(180deg, #f3e6dc 0%, #e9cbb6 60%, #dcb39c 100%); }
  .treatment-photo.chin { background: linear-gradient(90deg, #f2ecea 0%, #e8b8a8 55%, #d89a8a 75%, #7f98d2 100%); }
  .contact {
    height: 110px;
    background: var(--navy);
    color: var(--white);
    display: flex; flex-direction: column;
    justify-content: center; align-items: center;
    gap: 10px;
    font-size: 19px;
    font-weight: 500;
  }
  .contact-row { display: flex; gap: 14px; align-items: center; }
  .contact-item { display: flex; align-items: center; gap: 5px; }
  .contact-icon { width: 14px; height: 14px; }
</style>
</head>
<body>
  <main class="poster">
    <div class="poster-body">
      <div class="hero-photo" role="img" aria-label="Four women in profile facing each other across a soft cream background">
        <div class="hero-side left"></div>
        <div class="hero-center"></div>
        <div class="hero-side right"></div>
      </div>

      <header class="brand">
        <span class="brand-mark"></span>
        <h1 class="brand-name">LUMAWELL</h1>
      </header>

      <div class="divider"></div>
      <h2 class="tagline">REFRESH YOUR LOOK,<br>REVIVE YOUR SPIRIT.</h2>
      <div class="divider lower"></div>

      <section class="services">
        <h3 class="services-title">SERVICES WE OFFERED</h3>
        <p class="services-list">Neuromodulator Treatment (Quelvo)<br>and Dermal Fillers.</p>
      </section>

      <div class="treatment-strip">
        <div class="treatment-photo forehead" role="img" aria-label="Injection treatment on a client's forehead"></div>
        <div class="treatment-photo brow" role="img" aria-label="Injection near a client's eyebrow with eyes closed"></div>
        <div class="treatment-photo chin" role="img" aria-label="Gloved hands giving a filler injection at the chin"></div>
      </div>

      <footer class="contact">
        <div class="contact-row">
          <span class="contact-item">
            <svg class="contact-icon" viewBox="0 0 14 14"><circle cx="7" cy="7" r="7" fill="#c9a227"/><path d="M4.3 3.6l1.4-.3.7 1.7-.9.7a5 5 0 0 0 2.8 2.8l.7-.9 1.7.7-.3 1.4C7 9.9 4.1 7 4.3 3.6z" fill="#1f3a5c"/></svg>
            604-555-0148
          </span>
          <span class="contact-item">
            <svg class="contact-icon" viewBox="0 0 14 14"><circle cx="7" cy="7" r="7" fill="#c9a227"/><rect x="3.5" y="4.5" width="7" height="5" fill="none" stroke="#1f3a5c" stroke-width="1"/><path d="M3.5 4.5L7 7.3l3.5-2.8" fill="none" stroke="#1f3a5c" stroke-width="1"/></svg>
            info@lumawellpine.ca
          </span>
          <span class="contact-item">
            <svg class="contact-icon" viewBox="0 0 14 14"><circle cx="7" cy="7" r="7" fill="#c9a227"/><circle cx="7" cy="7" r="3.6" fill="none" stroke="#1f3a5c" stroke-width="1"/><path d="M3.4 7h7.2M7 3.4c-1.6 2-1.6 5.2 0 7.2M7 3.4c1.6 2 1.6 5.2 0 7.2" fill="none" stroke="#1f3a5c" stroke-width="0.8"/></svg>
            www.lumawellpine.ca
          </span>
        </div>
        <div class="contact-row">
          <span class="contact-item">
            <svg class="contact-icon" viewBox="0 0 14 14"><circle cx="7" cy="7" r="7" fill="#c9a227"/><path d="M7 3a2.6 2.6 0 0 1 2.6 2.6C9.6 7.6 7 10.8 7 10.8S4.4 7.6 4.4 5.6A2.6 2.6 0 0 1 7 3z" fill="#1f3a5c"/><circle cx="7" cy="5.6" r="1" fill="#c9a227"/></svg>
            204-205 27361 92 Ave, Surrey, V7K 2M4
          </span>
        </div>
      </footer>
    </div>
  </main>
</body>
</html>
```